Design some Business Cards for Birch Meadow

could someone please design some snazzy business cards for "Birch Meadow"
the website is birchmeadow.co.nz

the logo is attached

name : Harriet Doucan
Contact Number: 0224819357
email: harrietdouc@birchmeadow.co.nz
Slogan: Competitive prices, and personal service in the Wanganui district

The theme is green as its for a lawn mowing outfit!

```html
<!DOCTYPE html>
<html lang="en">
<head>
<meta charset="utf-8">
<title>Birch Meadow – Business Card</title>
<link rel="stylesheet" href="https://fonts.googleapis.com/css2?family=Ubuntu:wght@400&display=swap">
<style>
  :root {
    --page-bg: #e9eae6;
    --card-white: #ffffff;
    --green-light: #9db34b;
    --green-dark: #6e8a1d;
    --band-green: #7a931f;
    --text-green: #6a8420;
    --text-white: #ffffff;
  }
  * { margin: 0; padding: 0; box-sizing: border-box; }
  html, body {
    width: 1200px;
    height: 1168px;
    overflow: hidden;
    background: var(--page-bg);
    font-family: "Ubuntu", "Segoe UI", sans-serif;
  }
  .business-card {
    position: absolute;
    left: 80px;
    top: 295px;
    width: 1040px;
    height: 578px;
    background: var(--card-white);
    box-shadow: 0 6px 24px rgba(0,0,0,0.18);
    overflow: hidden;
  }
  .brand-panel {
    position: absolute;
    left: 0; top: 0;
    width: 470px;
    height: 100%;
    background: linear-gradient(180deg, var(--green-light) 0%, var(--green-dark) 100%);
  }
  .brand-mark {
    position: absolute;
    left: 175px;
    top: 95px;
  }
  .brand-name {
    position: absolute;
    left: 0;
    width: 470px;
    top: 318px;
    text-align: center;
    color: var(--text-white);
    font-size: 46px;
    font-weight: 400;
    letter-spacing: 0.5px;
  }
  .slogan-band {
    position: absolute;
    left: 470px;
    top: 440px;
    width: 570px;
    height: 58px;
    background: var(--band-green);
  }
  .slogan {
    position: absolute;
    left: 34px;
    top: 450px;
    color: var(--text-white);
    font-size: 27px;
    white-space: nowrap;
    letter-spacing: 0.2px;
  }
  .contact {
    position: absolute;
    left: 515px;
    top: 80px;
    color: var(--text-green);
  }
  .contact-name {
    font-size: 32px;
    margin-bottom: 58px;
  }
  .contact-line {
    font-size: 24px;
    line-height: 44px;
  }
</style>
</head>
<body>
  <article class="business-card">
    <section class="brand-panel">
      <svg class="brand-mark" width="120" height="120" viewBox="0 0 120 120" aria-hidden="true">
        <circle cx="60" cy="60" r="56" fill="var(--text-white)"/>
      </svg>
      <div class="brand-name">Birch Meadow</div>
    </section>

    <div class="slogan-band"></div>
    <p class="slogan">Competitive prices, and personal service in the Wanganui district</p>

    <section class="contact">
      <h1 class="contact-name" style="font-weight:400">Harriet Doucan</h1>
      <p class="contact-line">0224819357</p>
      <p class="contact-line">harrietdouc@birchmeadow.co.nz</p>
      <p class="contact-line">www.birchmeadow.co.nz</p>
    </section>
  </article>
</body>
</html>
```